Business Card for a finance professional

I need a business card design to introduce myself to a professional networking (mainly banks) and potential companies to hire and remember me. I would like to use black, grey, white and maybe gold/silver colors and maybe something with my initials(L R B F T). The final design should communicate seriousness, profissionalism and something innovative.

The basic informations in the card are: Name, e-mail, phone number and linkedin. (I'm thinking to put some directly short link to my linkedin account or maybe some app - non QR Code - to add my contacts to a phone directly.)

My name is Mariana Lopes Barbosa Ferraz da Trindade (I prefer to use only 'Mariana Lopes' or 'Mariana Trindade' but i'm open to other suggestions) and I have 26 years old (just if it helps to build based in my age).
Updates

Dear designers, I wish to thank your participation in this project! It was very difficult to choose one! Thank your for your work! Best regards and success. Mariana

Target Market(s)

Potential hires and big companies.

Industry/Entity Type

Finance

Requirements
Must have
• The informations required at the business card are:
Name: Mariana Lopes B. F. da Trindade
Email: mariana.lbf.trindade@caixapostal.example
Phone: +55 61 9043 5718
LinkedIn: http://br.redeprofissa.example/in/marianalt/
Nice to have
• Modern and innovative look.
I suggest to use the colors black, grey, white, gold and/or silver, but I'm open to other colors.
Should not have
• A message showing that I need to be hired. It's more to "know me and remember me" than "hire me please".

```html
<!DOCTYPE html>
<html lang="pt">
<head>
<meta charset="utf-8">
<title>Mariana Trindade – Business Card</title>
<link href="https://fonts.googleapis.com/css2?family=PT+Serif&family=Noto+Serif:wght@400&display=swap" rel="stylesheet">
<style>
  :root {
    --backdrop: #7b7467;
    --card-dark: #151515;
    --card-dark-edge: #222222;
    --silver: #d9d9d9;
    --silver-soft: #a9a9a9;
    --card-light: #ebebe9;
    --frame-line: #c9c9c6;
    --ink: #2b2b2b;
    --ink-soft: #555555;
  }
  * { box-sizing: border-box; margin: 0; padding: 0; }
  html, body { width: 1200px; height: 1000px; overflow: hidden; }
  body {
    background: var(--backdrop);
    display: flex;
    align-items: center;
    justify-content: center;
    gap: 60px;
  }
  .card {
    width: 520px;
    height: 300px;
    position: relative;
    box-shadow: 0 6px 18px rgba(0,0,0,0.35);
  }
  /* Front */
  .card-front {
    background: var(--card-dark);
    border: 1px solid var(--card-dark-edge);
    display: flex;
    align-items: center;
    justify-content: center;
  }
  .wordmark { display: flex; flex-direction: column; align-items: flex-start; }
  .wordmark-name {
    font-family: "PT Serif", Georgia, serif;
    font-size: 66px;
    line-height: 1;
    color: var(--silver);
    letter-spacing: 1px;
  }
  .wordmark-rule {
    width: 100%;
    height: 1px;
    background: var(--silver-soft);
    margin-top: 6px;
  }
  .wordmark-tagline {
    font-family: "Noto Serif", Georgia, serif;
    font-size: 17px;
    color: var(--silver-soft);
    letter-spacing: 2px;
    margin-top: 4px;
  }
  /* Back */
  .card-back {
    background: var(--card-light);
    display: flex;
    align-items: center;
    justify-content: center;
  }
  .card-frame {
    position: absolute;
    inset: 10px;
    border: 3px double var(--frame-line);
    pointer-events: none;
  }
  .contact { display: flex; flex-direction: column; align-items: center; }
  .contact-name {
    font-family: "PT Serif", Georgia, serif;
    font-size: 23px;
    color: var(--ink);
    padding: 0 4px 6px;
    border-bottom: 1px solid var(--ink);
  }
  .contact-list {
    list-style: none;
    margin-top: 10px;
    font-family: "Noto Serif", Georgia, serif;
    font-size: 13px;
    color: var(--ink);
    line-height: 1.6;
  }
  .contact-list li { display: flex; }
  .contact-label {
    width: 34px;
    text-align: right;
    padding-right: 6px;
    font-size: 11px;
    color: var(--ink-soft);
    align-self: center;
  }
</style>
</head>
<body>
  <section class="card card-front" aria-label="Card front">
    <div class="wordmark">
      <span class="wordmark-name">Mariana</span>
      <span class="wordmark-rule"></span>
      <span class="wordmark-tagline">finance professional</span>
    </div>
  </section>

  <section class="card card-back" aria-label="Card back">
    <div class="card-frame"></div>
    <div class="contact">
      <h1 class="contact-name">Mariana Lopes B. F. da Trindade</h1>
      <ul class="contact-list">
        <li><span class="contact-label">P:</span><span>+55 61 9043 5718</span></li>
        <li><span class="contact-label">E:</span><span>mariana.lbf.trindade@caixapostal.example</span></li>
        <li><span class="contact-label">In:</span><span>br.redeprofissa.example/in/marianalt</span></li>
      </ul>
    </div>
  </section>
</body>
</html>
```